Postcard Design

we need a post card design for our company in worth, illinois called Velmoran Dental lab we would like to see designs that use the colors blue and gray. We are a dental lab specializing in removable dentures and partials. These particular post cards are emphasizing doing relines and repairs the same day our address is 4870 N corbett ave worth I'll. Phone 708-555-0142

Industry/Entity Type

Dental

```html
<!DOCTYPE html>
<html lang="en">
<head>
<meta charset="utf-8">
<title>Velmoran Dental lab – Postcard</title>
<link href="https://fonts.googleapis.com/css2?family=Archivo+Narrow:wght@700&family=Lato:wght@400;700&family=Montserrat:wght@700&display=swap" rel="stylesheet">
<style>
  :root {
    --blue: #3a72b8;
    --dark: #3c3c3c;
    --stamp: #cfcfcf;
    --page: #ececec;
    --white: #ffffff;
    --text: #333333;
  }
  * { box-sizing: border-box; margin: 0; padding: 0; }
  html, body { width: 825px; height: 1200px; overflow: hidden; }
  body { background: var(--page); position: relative; font-family: "Lato", sans-serif; }

  .postcard {
    position: absolute; left: 95px; width: 638px; height: 495px;
    background: var(--white); overflow: hidden;
    box-shadow: 0 4px 14px rgba(0,0,0,.18);
  }
  .postcard--front { top: 83px; }
  .postcard--back { top: 622px; }
  .postcard__art { position: absolute; inset: 0; }

  .headline {
    position: absolute; font-family: "Archivo Narrow", sans-serif; font-weight: 700;
    font-size: 23px; line-height: 28.5px; white-space: nowrap;
  }
  .postcard--front .headline { left: 37px; top: 22px; color: var(--white); }
  .postcard--back .headline { left: 33px; top: 27px; color: var(--dark); }
  .headline__accent { color: var(--blue); }

  .portrait {
    position: absolute; top: 125px; width: 110px; height: 110px; border-radius: 50%;
    border: 5px solid var(--dark); box-shadow: 0 0 0 3px var(--white) inset;
    background: radial-gradient(circle at 50% 45%, #e8d2c2, #9fb6cf);
  }
  .portrait--left { left: 35px; }
  .portrait--right { left: 168px; }

  .body-copy {
    position: absolute; font-size: 11.4px; line-height: 14.5px; color: var(--text); width: 292px;
  }
  .postcard--front .body-copy { left: 42px; top: 258px; }
  .postcard--back .body-copy { left: 42px; top: 377px; }

  .bullets {
    position: absolute; list-style: none; color: var(--white); font-size: 16.5px; line-height: 20.5px;
    white-space: nowrap;
  }
  .bullets li { position: relative; padding-left: 22px; }
  .bullets li::before {
    content: ""; position: absolute; left: 0; top: 7px; width: 7px; height: 7px;
    border-radius: 50%; background: var(--dark);
  }
  .postcard--front .bullets { left: 42px; top: 354px; }
  .postcard--back .bullets { left: 34px; top: 262px; }

  .brand {
    position: absolute; left: 365px; top: 48px; display: flex; align-items: center; gap: 14px;
  }
  .brand__dot { width: 80px; height: 80px; border-radius: 50%; background: var(--blue); flex: none; }
  .brand__name {
    font-family: "Lato", sans-serif; font-weight: 700; color: var(--blue);
    font-size: 27px; line-height: 31px;
  }

  .hero-photo {
    position: absolute; left: 410px; top: 142px; width: 228px; height: 315px;
    background: linear-gradient(160deg, #f1ece7 0%, #e3c3a8 45%, #cfd3d9 100%);
    border-radius: 120px 0 0 0;
  }

  .contact {
    position: absolute; left: 33px; top: 165px; color: var(--white); white-space: nowrap;
    font-family: "Montserrat", sans-serif; font-weight: 700; font-size: 29px; line-height: 35px;
  }

  .stamp-box { position: absolute; left: 539px; top: 28px; width: 63px; height: 63px; background: var(--stamp); }
</style>
</head>
<body>

<section class="postcard postcard--front">
  <svg class="postcard__art" viewBox="0 0 638 495" width="638" height="495" aria-hidden="true">
    <defs>
      <linearGradient id="frontPanel" x1="0" y1="0" x2="0" y2="1">
        <stop offset="0" stop-color="#ffffff"/>
        <stop offset="1" stop-color="#dedede"/>
      </linearGradient>
      <clipPath id="frontLeft">
        <path d="M0 0 H375 C342 120 347 230 367 300 C387 370 392 410 382 457 H0 Z"/>
      </clipPath>
    </defs>
    <g clip-path="url(#frontLeft)">
      <rect x="0" y="0" width="638" height="457" fill="url(#frontPanel)"/>
      <rect x="0" y="0" width="638" height="162" fill="var(--blue)"/>
      <rect x="0" y="172" width="325" height="17" fill="var(--dark)"/>
      <path d="M22 345 Q22 330 37 330 H345 V412 Q345 435 322 435 H22 Z" fill="var(--blue)"/>
    </g>
    <path d="M385 0 C352 120 357 230 377 300 C397 370 402 410 392 457" fill="none" stroke="var(--blue)" stroke-width="5"/>
    <rect x="0" y="457" width="638" height="5" fill="var(--blue)"/>
    <rect x="0" y="462" width="638" height="33" fill="var(--dark)"/>
  </svg>

  <h1 class="headline">We are a dental lab<br>specializing in removable<br>dentures and partials</h1>

  <div class="portrait portrait--left" role="img" aria-label="Photo of a patient smiling in the dental chair"></div>
  <div class="portrait portrait--right" role="img" aria-label="Photo of a smiling young woman"></div>

  <p class="body-copy">Lorem ipsum dolor sit amet, consectetuer adipiscing elit, sed diam nonummy nibh euismod tincidunt ut laoreet dolore magna aliquam erat volutpat.</p>

  <ul class="bullets">
    <li>Lorem ipsum dolor sit amet lorem</li>
    <li>Lorem ipsum dolor sit amet lorem</li>
    <li>Lorem ipsum dolor sit amet lorem</li>
  </ul>

  <div class="brand">
    <span class="brand__dot"></span>
    <span class="brand__name">Velmoran<br>Dental lab</span>
  </div>

  <div class="hero-photo" role="img" aria-label="Photo of a smiling senior couple"></div>
</section>

<section class="postcard postcard--back">
  <svg class="postcard__art" viewBox="0 0 638 495" width="638" height="495" aria-hidden="true">
    <defs>
      <clipPath id="backLeft">
        <path d="M0 0 H377 C337 80 342 150 357 200 C387 280 392 330 372 457 H0 Z"/>
      </clipPath>
    </defs>
    <g clip-path="url(#backLeft)">
      <rect x="0" y="136" width="310" height="8" fill="var(--dark)"/>
      <rect x="0" y="144" width="638" height="208" fill="var(--blue)"/>
    </g>
    <path d="M385 0 C345 80 350 150 365 200 C395 280 400 330 380 457" fill="none" stroke="var(--blue)" stroke-width="5"/>
    <rect x="0" y="456" width="638" height="5" fill="var(--blue)"/>
    <rect x="0" y="461" width="638" height="34" fill="var(--dark)"/>
  </svg>

  <h2 class="headline">We are a dental lab<br><span class="headline__accent">specializing in removable</span><br>dentures and partials</h2>

  <p class="contact">Contact us now!<br>At: 708-555-0142</p>

  <ul class="bullets">
    <li>Same-day relines and repairs</li>
    <li>Removable dentures and partials</li>
    <li>4870 N corbett ave, Worth IL</li>
  </ul>

  <p class="body-copy">Lorem ipsum dolor sit amet, consectetuer adipiscing elit, sed diam nonummy nibh euismod tincidunt ut laoreet dolore magna aliquam erat volutpat.</p>

  <div class="stamp-box"></div>
</section>

</body>
</html>
```